Sudsy Harbor Laundromat Wordpress Design

We need a Wordpress website design for our laundromat, Sudsy Harbor Atlanta, at www.sudsyharborlaunder.example. We would like to have 6 pages: Home, About Us, Services, Locations, Reviews and Contact us. We will provide content for the text on each page. What we do: We are a full service laundromat that provides dry cleaning drop off, professional laundry services, wash dry fold and self service laundry to the local community. We would like to use the color scheme from our logo to convey a warm, safe, and bright business that caters to its diverse community.
Updates

I like the structure of this laundromat website: http://www.tumblewashexample.com/ Using my logo and color scheme in the above referenced website is what. Am looking for. The photos attached to the project with the female model should be used as a primary focus and supplemented by actual photos of the equipment.

Target Market(s)

Our target market is a diverse group of people from Midtown Atlanta - LGBTQ community /Locals/Regulars that have been coming to laundromat for 30 years.

Industry/Entity Type

Laundromat

Coding

Coded - Design and coding required

Number of Pages Required

5+ page

Font styles to use
Sans Serif

Colors
0054AA
0677BA
7BADD7
CADEEF
E8F1F8

Requirements
Must have
• Feature this video on the main page: https://videos.example.net/wq7PzrT2kLm

```html
<!DOCTYPE html>
<html lang="en">
<head>
<meta charset="utf-8">
<title>Sudsy Harbor Laundromat</title>
<link rel="stylesheet" href="https://fonts.googleapis.com/css2?family=Rubik:wght@500;600;700&family=Roboto:wght@400;500;700&family=Caveat:wght@400;500&display=swap">
<style>
:root{
  --blue:#0054aa;
  --blue-mid:#0677ba;
  --blue-soft:#7badd7;
  --blue-pale:#cadeef;
  --blue-mist:#e8f1f8;
  --heading:#1a56a6;
  --cyan:#2bc6f5;
  --navy:#0b3a75;
  --panel:#0e3f7e;
  --footer:#1c2382;
  --text:#7d8590;
  --violet:#6a2fd1;
  --white:#ffffff;
}
*{box-sizing:border-box;margin:0;padding:0}
html,body{width:1200px;height:4147px;overflow:hidden}
body{font-family:"Roboto",sans-serif;color:var(--text);background:var(--white);position:relative}
.abs{position:absolute}
.script{font-family:"Caveat",cursive;color:var(--cyan);font-size:22px}
.h2{font-family:"Rubik",sans-serif;font-weight:500;color:var(--heading);font-size:29px}
.btn{display:flex;align-items:center;justify-content:center;gap:14px;font-weight:700;font-size:11px;border-radius:2px}
.btn-blue{background:var(--blue);color:var(--white)}

/* top bar */
.topbar{left:0;top:0;width:1200px;height:24px;background:var(--navy);color:var(--white);font-size:9px;display:flex;align-items:center;padding:0 38px}
.topbar span{display:flex;align-items:center;gap:5px;margin-right:22px;white-space:nowrap}
.topbar .social{margin-left:auto;display:flex;gap:6px}
.dot{width:15px;height:15px;border-radius:50%;background:var(--cyan);display:inline-block}

/* header */
.header{left:0;top:24px;width:1200px;height:87px;background:var(--white);border-bottom:1px solid #e6ebf1}
.brand{left:86px;top:20px;display:flex;align-items:center;gap:8px;font-family:"Rubik",sans-serif;font-weight:600;color:var(--blue);font-size:18px;line-height:1.1;width:200px}
.brand i{width:14px;height:14px;border-radius:50%;background:var(--cyan);flex:none}
.brand-div{left:303px;top:0;width:1px;height:87px;background:#e6ebf1}
.nav{right:104px;top:0;height:87px;display:flex;align-items:center;gap:24px;font-size:11.5px;font-weight:700;color:var(--heading)}
.nav a{position:relative;height:87px;display:flex;align-items:center}
.nav a.active::after{content:"";position:absolute;left:0;right:0;bottom:0;height:3px;background:var(--cyan)}

/* hero */
.hero{left:0;top:111px;width:1200px;height:586px;background:linear-gradient(100deg,#5d6670 0%,#7d8894 45%,#9aa4ae 75%,#6d7781 100%)}
.hero-script{left:90px;top:155px;font-size:22px}
.hero-title{left:90px;top:186px;font-family:"Rubik",sans-serif;font-weight:600;color:var(--cyan);font-size:60px;line-height:62px;white-space:nowrap}
.hero-sub{left:90px;top:332px;color:var(--cyan);font-weight:700;font-size:12px}
.hero .b1{left:89px;top:377px;width:153px;height:53px}
.hero .b2{left:265px;top:377px;width:135px;height:53px;background:var(--white);color:var(--blue)}
.play{left:992px;top:233px;width:120px;height:120px;border-radius:50%;border:2px solid var(--white);display:flex;align-items:center;justify-content:center}
.play-in{width:58px;height:58px;border-radius:50%;background:var(--white);display:flex;align-items:center;justify-content:center}
.play-label{left:992px;top:360px;width:120px;text-align:center;color:var(--white);font-size:9px;font-weight:700;letter-spacing:2px}
.hero-arrow{top:275px}
.dots{display:flex;gap:8px}
.dots i{display:block;height:4px;width:18px;background:rgba(255,255,255,.5);border-radius:2px}
.dots i.on{width:24px;background:var(--white)}

/* about */
.about{left:0;top:697px;width:1200px;height:737px;background:#f2f6fb}
.about-photo{left:611px;top:0;width:501px;height:737px;background:linear-gradient(180deg,#a9d6d3 0%,#cfdcd8 45%,#b9bfc3 75%,#9aa1a6 100%)}
.about-script{left:176px;top:130px}
.about-h{left:176px;top:170px;font-size:28px}
.about-p{left:176px;width:315px;font-size:12.5px;line-height:21.5px}
.about .btn{left:176px;top:477px;width:122px;height:38px}

/* services */
.services{left:0;top:1434px;width:1200px;height:1205px;background:#f5f8fc}
.center{left:0;width:1200px;text-align:center}
.card{width:325px;height:374px;background:var(--white);box-shadow:0 6px 24px rgba(20,60,120,.06)}
.card .bar{position:absolute;left:0;top:0;width:285px;height:4px;background:var(--blue)}
.card .icon{position:absolute;left:40px;top:40px;width:62px;height:62px}
.card h3{position:absolute;left:40px;top:140px;font-family:"Rubik",sans-serif;font-weight:600;color:var(--heading);font-size:17px}
.card p{position:absolute;left:40px;top:178px;width:250px;font-size:11px;line-height:20px}
.card .btn{position:absolute;left:40px;top:296px;width:246px;height:38px;justify-content:space-between;padding:0 24px;background:var(--navy);color:var(--white)}
.sdots{display:flex;gap:6px;justify-content:center}
.sdots i{display:block;width:28px;height:4px;background:var(--cyan);border-radius:2px}
.sdots i.dark{width:16px;background:var(--navy)}

/* machines */
.machines{left:29px;top:2639px;width:1128px;height:651px;background:var(--panel);border-radius:4px}
.machines .script{position:absolute;left:61px;top:80px}
.mphoto{top:161px;width:321px;height:367px;background:linear-gradient(180deg,#e8ece9 0%,#9fb6b3 35%,#7f8a8f 70%,#b5b9bb 100%)}
.machines .dots{position:absolute;left:537px;top:559px}

/* reviews */
.reviews{left:0;top:3290px;width:1200px;height:480px;background:var(--white)}
.quote{left:257px;top:226px;width:686px;font-size:14px;line-height:23px;color:#3b3f46;text-align:center}
.avatar{left:530px;top:332px;width:64px;height:64px;border-radius:50%;background:linear-gradient(180deg,#d9dfe7,#aeb8c4)}
.rname{left:612px;top:334px;font-size:21px;color:var(--violet)}
.rtitle{left:638px;top:366px;font-size:11px;color:var(--text)}

/* footer */
.footer{left:0;top:3770px;width:1200px;height:377px;background:var(--footer);color:#c9cdf0}
.fcol{top:105px}
.fcol h4{font-family:"Rubik",sans-serif;font-weight:500;color:var(--white);font-size:13px;margin-bottom:30px}
.fcol li{list-style:none;font-size:11px;line-height:26px}
.query{left:953px;top:94px;width:158px;height:47px;background:var(--blue);color:var(--white);font-weight:700;font-size:11px;display:flex;align-items:center;justify-content:center;border-radius:2px}
.fsocial{left:1003px;top:178px;display:flex;gap:14px}
.fsocial i{width:26px;height:26px;border-radius:50%;border:1.5px solid var(--white);display:flex;align-items:center;justify-content:center}
.fsocial i::after{content:"";width:14px;height:14px;border-radius:50%;background:var(--cyan)}
</style>
</head>
<body>

<div class="abs topbar">
  <span><svg width="9" height="9" viewBox="0 0 24 24"><path fill="#fff" d="M6.6 10.8a15 15 0 0 0 6.6 6.6l2.2-2.2c.3-.3.7-.4 1-.2 1.1.4 2.3.6 3.6.6.6 0 1 .4 1 1V20c0 .6-.4 1-1 1A17 17 0 0 1 3 4c0-.6.4-1 1-1h3.5c.6 0 1 .4 1 1 0 1.3.2 2.5.6 3.6.1.3 0 .7-.2 1z"/></svg>Phone: +1 404 555 0193</span>
  <span><svg width="9" height="9" viewBox="0 0 24 24"><path fill="#fff" d="M2 5h20v14H2zM4 7l8 6 8-6"/></svg>Email: hello@sudsyharbor.example</span>
  <span><svg width="9" height="9" viewBox="0 0 24 24"><circle cx="12" cy="12" r="10" fill="#fff"/></svg>Hours: Mon-Sat: 7am – 9pm</span>
  <span><svg width="8" height="10" viewBox="0 0 24 30"><path fill="#fff" d="M12 0a11 11 0 0 0-11 11c0 8 11 19 11 19s11-11 11-19A11 11 0 0 0 12 0z"/></svg>Get Directions</span>
  <div class="social"><i class="dot"></i><i class="dot"></i><i class="dot"></i></div>
</div>

<header class="abs header">
  <div class="abs brand"><i></i>Sudsy Harbor Laundromat</div>
  <div class="abs brand-div"></div>
  <nav class="abs nav">
    <a class="active">HOME</a><a>ABOUT US</a><a>SERVICES</a><a>LOCATIONS</a><a>REVIEWS</a><a>CONTACT</a>
  </nav>
</header>

<section class="abs hero" role="img" aria-label="Laundromat interior with rows of washing machines">
  <div class="abs script hero-script">Lorem Ipsum Dolor Sit Amet</div>
  <h1 class="abs hero-title">Lorem Ipsum Dolor Sit<br>Amet Dummy Text</h1>
  <p class="abs hero-sub">Lorem ipsum dolor sit amet, consectetur adipiscing elit, sed do eiusmod tempor</p>
  <div class="abs btn btn-blue b1">More About Us <svg width="10" height="10" viewBox="0 0 10 10"><path d="M1 5h8M5 1l4 4-4 4" stroke="#fff" stroke-width="1.5" fill="none"/></svg></div>
  <div class="abs btn b2">Our Services</div>
  <div class="abs play"><div class="play-in"><svg width="16" height="18" viewBox="0 0 16 18"><path d="M2 1l13 8-13 8z" fill="var(--navy)"/></svg></div></div>
  <div class="abs play-label">OUR VIDEO</div>
  <svg class="abs hero-arrow" style="left:30px" width="18" height="34" viewBox="0 0 18 34"><path d="M16 2L2 17l14 15" stroke="#fff" stroke-width="1.5" fill="none"/></svg>
  <svg class="abs hero-arrow" style="left:1152px" width="18" height="34" viewBox="0 0 18 34"><path d="M2 2l14 15L2 32" stroke="#fff" stroke-width="1.5" fill="none"/></svg>
  <div class="abs dots" style="left:576px;top:519px"><i class="on"></i><i></i></div>
</section>

<section class="abs about">
  <div class="abs script about-script">Lorem Ipsum Dolor Sit Amet</div>
  <h2 class="abs h2 about-h">Lorem Ipsum Dolor Sit</h2>
  <p class="abs about-p" style="top:233px">Lorem ipsum dolor sit amet, consectetur adipiscing elit, sed do eiusmod tempor incididunt ut labore et dolore magna aliqua. Ut enim ad minim veniam, quis nostrud exercitation ullamco laboris nisi ut aliquip ex ea commodo consequat. nt in culpa qui officia deserunt mollit anim id est laborum.</p>
  <p class="abs about-p" style="top:380px">Lorem ipsum dolor sit amet, consectetur adipiscing elit, sed do eiusmod tempor incididunt ut labore et dolore</p>
  <div class="abs btn btn-blue">Read More <svg width="10" height="10" viewBox="0 0 10 10"><path d="M1 5h8M5 1l4 4-4 4" stroke="#fff" stroke-width="1.5" fill="none"/></svg></div>
  <div class="abs about-photo" role="img" aria-label="Woman in a blue dress pushing a laundry cart past washers under a vintage sign"></div>
</section>

<section class="abs services">
  <div class="abs center script" style="top:96px">Our Services</div>
  <h2 class="abs center h2" style="top:135px">Lorem Ipsum Dolor Sit Amet</h2>

  <div class="abs card" style="left:89px;top:211px"><i class="bar"></i>
    <svg class="icon" viewBox="0 0 62 62"><circle cx="24" cy="24" r="22" fill="var(--blue-mist)"/><circle cx="33" cy="33" r="22" fill="none" stroke="var(--blue)" stroke-width="2"/><circle cx="33" cy="33" r="16" fill="none" stroke="var(--blue)" stroke-width="2"/><path d="M22 44L44 22" stroke="var(--blue)" stroke-width="2"/></svg>
    <h3>Dry Clean Service</h3>
    <p>Using our national disinfection expertise and experience in facilities, we handle the unique has created by experts are essential.</p>
    <div class="btn">Read More <span>→</span></div></div>

  <div class="abs card" style="left:438px;top:211px"><i class="bar"></i>
    <svg class="icon" viewBox="0 0 62 62"><circle cx="24" cy="24" r="22" fill="var(--blue-mist)"/><path d="M16 24h20l-3 28H19z" fill="none" stroke="var(--blue)" stroke-width="2"/><rect x="40" y="18" width="12" height="34" rx="2" fill="none" stroke="var(--blue)" stroke-width="2"/></svg>
    <h3>Leaather And Suede</h3>
    <p>If you are tired of replacing your janitorial company due to their complacency , its time to go with the experts who believe that a job.</p>
    <div class="btn">Read More <span>→</span></div></div>

  <div class="abs card" style="left:786px;top:211px"><i class="bar"></i>
    <svg class="icon" viewBox="0 0 62 62"><circle cx="24" cy="24" r="22" fill="var(--blue-mist)"/><path d="M12 34c0-10 10-16 30-14v14z" fill="none" stroke="var(--blue)" stroke-width="2"/><path d="M14 38v8M20 38v8M26 38v8M32 38v8M38 38v8" stroke="var(--blue)" stroke-width="2"/></svg>
    <h3>Wash, Dry, Fold</h3>
    <p>Using proprietary products, practices and equipment, we take care of inspect our work to ensure the results meet our high standards.</p>
    <div class="btn">Read More <span>→</span></div></div>

  <div class="abs card" style="left:89px;top:636px"><i class="bar"></i>
    <svg class="icon" viewBox="0 0 62 62"><circle cx="24" cy="24" r="22" fill="var(--blue-mist)"/><rect x="8" y="26" width="46" height="30" rx="3" fill="none" stroke="var(--blue)" stroke-width="2"/><circle cx="26" cy="41" r="9" fill="none" stroke="var(--blue)" stroke-width="2"/><path d="M22 26l-4-14h16l-4 14" fill="none" stroke="var(--blue)" stroke-width="2"/></svg>
    <h3>Over 50 Machines</h3>
    <p>Whether it is a one-time janitorial cleaning or a single specialty cleaning such our cleaning experts serve you with the professionalism.</p>
    <div class="btn">Read More <span>→</span></div></div>

  <div class="abs card" style="left:438px;top:636px"><i class="bar"></i>
    <svg class="icon" viewBox="0 0 62 62"><circle cx="24" cy="24" r="22" fill="var(--blue-mist)"/><path d="M18 14l18 22M26 12l18 22M12 22l20 26 10 6 8-8-4-10" fill="none" stroke="var(--blue)" stroke-width="2"/></svg>
    <h3>Cool-comfortable-clean</h3>
    <p>We will help maintain a clean, healthy work environment in your facility with a cleaning schedule that matches your business</p>
    <div class="btn">Read More <span>→</span></div></div>

  <div class="abs card" style="left:786px;top:636px"><i class="bar"></i>
    <svg class="icon" viewBox="0 0 62 62"><circle cx="24" cy="24" r="22" fill="var(--blue-mist)"/><circle cx="33" cy="33" r="22" fill="none" stroke="var(--blue)" stroke-width="2"/><circle cx="33" cy="33" r="16" fill="none" stroke="var(--blue)" stroke-width="2"/><path d="M22 44L44 22" stroke="var(--blue)" stroke-width="2"/></svg>
    <h3>Best In Business</h3>
    <p>Using our national disinfection expertise and experience in facilities, we handle the unique has created by experts are essential.</p>
    <div class="btn">Read More <span>→</span></div></div>

  <div class="abs sdots" style="left:0;width:1200px;top:1119px"><i></i><i class="dark"></i></div>
</section>

<section class="abs machines">
  <div class="script">Our Machines</div>
  <div class="abs mphoto" style="left:60px" role="img" aria-label="Stainless front-load washers in the laundromat"></div>
  <div class="abs mphoto" style="left:403px" role="img" aria-label="Row of washing machines with a laundry cart"></div>
  <div class="abs mphoto" style="left:749px" role="img" aria-label="Stainless front-load washers in the laundromat"></div>
  <div class="dots"><i class="on" style="width:30px"></i><i></i></div>
</section>

<section class="abs reviews">
  <div class="abs center script" style="top:112px">Reviews</div>
  <h2 class="abs center h2" style="top:152px">What They Say About Us</h2>
  <p class="abs quote">Consectetur adipiscing elit, sed do eiusmod tempor incididunt ut labore et dolore magna aliqua. Quis ipsum suspendisse ultrices gravida. Risus commodo viverra maecenas accumsan lacus vel facilisis por incididunt ut labore et dolore mas.</p>
  <svg class="abs" style="left:180px;top:312px" width="10" height="18" viewBox="0 0 10 18"><path d="M9 1L1 9l8 8" stroke="#e0447a" stroke-width="1.5" fill="none"/></svg>
  <svg class="abs" style="left:1002px;top:312px" width="10" height="18" viewBox="0 0 10 18"><path d="M1 1l8 8-8 8" stroke="#e0447a" stroke-width="1.5" fill="none"/></svg>
  <div class="abs avatar" role="img" aria-label="Customer portrait"></div>
  <div class="abs rname">Mara Quill</div>
  <div class="abs rtitle">lorem title</div>
</section>

<footer class="abs footer">
  <div class="abs fcol" style="left:89px;width:240px">
    <h4>Quick Contact</h4>
    <p style="font-size:11px;line-height:19px">If you have any questions or need help, feel free to contact with our team.</p>
    <p style="display:flex;align-items:center;gap:10px;color:var(--cyan);font-weight:700;font-size:16px;margin-top:14px"><svg width="12" height="12" viewBox="0 0 24 24"><path fill="var(--cyan)" d="M6.6 10.8a15 15 0 0 0 6.6 6.6l2.2-2.2c.3-.3.7-.4 1-.2 1.1.4 2.3.6 3.6.6.6 0 1 .4 1 1V20c0 .6-.4 1-1 1A17 17 0 0 1 3 4c0-.6.4-1 1-1h3.5c.6 0 1 .4 1 1 0 1.3.2 2.5.6 3.6.1.3 0 .7-.2 1z"/></svg>0104555017</p>
    <p style="font-size:11px;margin-top:14px">Harbor Row, Midtown</p>
    <p style="font-size:11px;margin-top:18px;color:var(--white);font-weight:700;display:flex;align-items:center;gap:6px"><svg width="8" height="10" viewBox="0 0 24 30"><path fill="#fff" d="M12 0a11 11 0 0 0-11 11c0 8 11 19 11 19s11-11 11-19A11 11 0 0 0 12 0z"/></svg>Get Directions</p>
  </div>
  <div class="abs fcol" style="left:350px"><h4>Company</h4><ul><li>About Us</li><li>Leadership Team</li><li>News &amp; Media</li><li>How It Works</li><li>Contacts</li></ul></div>
  <div class="abs fcol" style="left:524px"><h4>Services</h4><ul><li>Services 1</li><li>Services 2</li><li>Services 3</li><li>Services 4</li><li>Services 5</li><li>Services 6</li></ul></div>
  <div class="abs fcol" style="left:697px"><h4>Support</h4><ul><li>Become A Franchise</li><li>Terms &amp; Conditions</li><li>Cleaning Tips</li><li>Products</li></ul></div>
  <div class="abs query">Query Anytime</div>
  <div class="abs fsocial"><i></i><i></i><i></i></div>
</footer>

</body>
</html>
```